Brightwell Works Capability Statement 2019

this document will be used to draw new business in so it NEEDS to be engaging and the prospective client will need to want to flip the page and read on.
this will be an engaging, ultra modern capability statement.
Pages i need created including text as per attachments capability statement 2018 REV
Fresh new Photos will need to be taken from from photo stock or similar site please do not use photos on existing attachments
Logo attached
Updates

Target Market(s)

Commercial building, facility managers, asset managers, strata markets

Industry/Entity Type

Construction Company

Colors

Designer to choose colors to be used in the design.

Requirements
Must have
• fresh, ultra modern and engaging.
• needs very fresh and crisp images, visually appealing colour scheme that draws the reader in
• - Referencing our QLD branch - covering the eastern seaboard
• - professional outfit
• - designs need to go all the way to edge of page
Nice to have
• all details in must haves
Should not have
• outdated colour scheme, outdated old - pixelated photos , not cropped in or border

```html
<!DOCTYPE html>
<html lang="en">
<head>
<meta charset="utf-8">
<title>Brightwell Works Capability Statement</title>
<link href="https://fonts.googleapis.com/css2?family=Montserrat:wght@400;500;600;700&display=swap" rel="stylesheet">
<style>
  :root {
    --orange: #f28a22;
    --navy: #252a6b;
    --ink: #1c1c2a;
    --paper: #ffffff;
    --backdrop: #7b7b7b;
    --dots: #2a3080;
  }
  * { box-sizing: border-box; margin: 0; padding: 0; }
  html, body { width: 1200px; height: 973px; overflow: hidden; }
  body {
    background: var(--backdrop);
    font-family: "Montserrat", sans-serif;
    color: var(--ink);
    position: relative;
  }
  .spread {
    position: absolute;
    left: 40px;
    width: 1120px;
    height: 450px;
    display: flex;
    box-shadow: 0 6px 18px rgba(0,0,0,.35);
  }
  .spread--services { top: 24px; }
  .spread--safety { top: 499px; }
  .page {
    position: relative;
    width: 560px;
    height: 450px;
    background: var(--paper);
    overflow: hidden;
    font-size: 8px;
    line-height: 1.28;
  }
  .page--navy { background: var(--navy); color: #fff; }
  .page-number {
    position: absolute;
    width: 64px; height: 64px;
    background: var(--orange);
    color: #fff;
    font-weight: 600;
    font-size: 10px;
    display: flex;
    align-items: center;
    justify-content: center;
  }
  .page-number--left { left: -16px; bottom: -16px; border-radius: 0 64px 0 0; padding: 0 0 12px 10px; }
  .page-number--right { right: -16px; bottom: -16px; border-radius: 64px 0 0 0; padding: 0 10px 12px 0; }
  .page-heading {
    position: absolute;
    font-weight: 600;
    font-size: 20px;
    line-height: 1.05;
    letter-spacing: .5px;
    text-transform: uppercase;
  }
  .page-heading .accent { color: var(--orange); display: block; }
  .page-heading .base { color: var(--navy); display: block; }
  .page--navy .page-heading .base { color: #fff; }
  .dotted-rule {
    position: absolute;
    border-top: 1.5px dotted var(--dots);
  }
  .dotted-stem {
    position: absolute;
    border-left: 1.5px dotted var(--dots);
  }
  .page--navy .dotted-rule, .page--navy .dotted-stem { border-color: #9ea3d6; }
  .block { position: absolute; }
  .block-title { color: var(--orange); font-weight: 600; font-size: 10px; margin-bottom: 2px; }
  .bullets { list-style: none; margin-top: 6px; }
  .bullets li { position: relative; padding-left: 11px; }
  .bullets li::before {
    content: ""; position: absolute; left: 0; top: 3px;
    width: 5px; height: 5px; border-radius: 50%; background: var(--orange);
  }
  .photo-circle {
    position: absolute;
    border-radius: 50%;
    border: 2.5px solid var(--orange);
  }
  .brand {
    position: absolute;
    right: 26px;
    text-align: right;
  }
  .brand-name { font-weight: 700; font-size: 15px; color: var(--orange); line-height: 1; }
  .brand-tag { font-size: 7px; color: #fff; margin-top: 2px; }
  .page--plain .brand-tag { color: var(--navy); }
  .em-brand { color: var(--navy); font-weight: 600; }
  .page--navy .em-brand { color: #fff; }
  p + p { margin-top: 7px; }
  .photo-rect { position: absolute; }
</style>
</head>
<body>

<div class="spread spread--services">
  <section class="page">
    <h1 class="page-heading" style="left:52px; top:48px;">
      <span class="accent">Core services</span><span class="base">and capabilities</span>
    </h1>
    <div class="dotted-rule" style="left:170px; top:98px; width:130px;"></div>
    <div class="dotted-stem" style="left:170px; top:98px; height:40px;"></div>

    <div class="block" style="left:182px; top:104px; width:340px;">
      <div class="block-title">Painting</div>
      <p>Award winning specialists in large-scale internal and external painting for multi-storey strata and commercial buildings, recognised for our expertise, professional finishes and painting projects for buildings with difficult access.</p>
      <ul class="bullets">
        <li>Exterior strata building painting</li>
        <li>Internal strata or commercial painting</li>
        <li>Structured maintenance painting for your individual property</li>
        <li>Apartment or unit interior painting (walls, ceilings, doors and window frames)</li>
        <li>Common areas painting (foyer, laundry or garbage rooms)</li>
        <li>Difficult-access sites (such as multi-storey strata or heritage commercial buildings)</li>
      </ul>
    </div>
    <div class="photo-circle" role="img" aria-label="Painter rolling paint onto a bright interior floor" style="left:50px; top:150px; width:100px; height:100px; background:radial-gradient(circle at 45% 40%, #e6ecef, #a9b4bb);"></div>

    <div class="block" style="left:182px; top:272px; width:345px;">
      <div class="block-title">Waterproofing</div>
      <p>Providing protective waterproofing for strata, commercial or residential property. Our experience in difficult-access strata and commercial waterproofing jobs over 20 years means we have the team in place to complete your waterproofing job quickly with minimum disruption to owners and tenants.</p>
      <ul class="bullets">
        <li>Roof top membranes waterproofing and drainage works</li>
        <li>Balconies waterproofing and drainage works</li>
        <li>Basement waterproofing and drainage works</li>
        <li>Common areas in apartment blocks or commercial buildings</li>
      </ul>
      <p style="margin-top:7px;">We use only the latest technologies and products including torch-on membranes, liquid epoxy and water-based membranes, to ensure the treatment lasts longer.</p>
    </div>
    <div class="photo-circle" role="img" aria-label="Close-up of grey tiled surface with waterproofing" style="left:55px; top:300px; width:100px; height:100px; background:radial-gradient(circle at 40% 40%, #c9cdd1, #7f868c);"></div>

    <div class="page-number page-number--left">6</div>
  </section>

  <section class="page page--navy">
    <div class="brand" style="top:22px;">
      <div class="brand-name">Brightwell Works</div>
      <div class="brand-tag">strata painting &amp; remedial repair</div>
    </div>

    <div class="photo-circle" role="img" aria-label="Hands laying a pale floor tile" style="left:48px; top:72px; width:92px; height:92px; background:radial-gradient(circle at 50% 40%, #eceae6, #a49c94);"></div>
    <div class="block" style="left:160px; top:62px; width:360px;">
      <div class="block-title">Tiling</div>
      <p>We have a reputation for outstanding tiling projects with our clients. Before we begin to lay tiles, we need to know that the underlying surface is watertight and dry which is why we suggest that you use <span class="em-brand">Brightwell Works</span> for both your waterproofing and tiling needs. When it comes to tiling common areas in your strata or commercial property, we need to manage risk and liability to prevent anyone slipping on common-area tiles and injuring themselves. To mitigate this issue, we'll help you understand the slip rating on your tiles before you make your final choice. Our team know their tiles and can assure the finished job will be perfectly finished and pleasing to look at.</p>
    </div>

    <div class="photo-circle" role="img" aria-label="Scaffolding around a building under repair against blue sky" style="left:48px; top:196px; width:88px; height:88px; background:radial-gradient(circle at 50% 35%, #7fb1e0, #6a5548);"></div>
    <div class="block" style="left:160px; top:192px; width:360px;">
      <div class="block-title">Spalling Repairs</div>
      <p>We use only the latest technologies (including Veltra and Crystaseal) to stop unsightly and dangerous concrete cancer and drummy cement render in strata and commercial buildings:</p>
      <ul class="bullets" style="margin-top:2px;">
        <li>Concrete floors</li>
        <li>Slab edges, beams and soffits</li>
        <li>Cement render walls</li>
        <li>Basements</li>
        <li>Ceilings</li>
      </ul>
    </div>

    <h2 class="page-heading" style="left:40px; top:300px;">
      <span><span style="color:var(--orange)">Competitive </span><span style="color:#fff">skills</span></span>
    </h2>
    <div class="dotted-rule" style="left:100px; top:325px; width:150px;"></div>
    <div class="dotted-stem" style="left:100px; top:325px; height:38px;"></div>
    <div class="block" style="left:112px; top:330px; width:420px; line-height:1.22;">
      <div class="block-title">We provide:</div>
      <ul class="bullets" style="margin-top:0;">
        <li>Itemised written quotations with fixed lump sum contracts</li>
        <li>Large-scale commercial and strata experience</li>
        <li>Sydney-wide coverage</li>
        <li>Flexibility in rescheduling job start dates</li>
        <li>30 full-time painters and tradespeople</li>
        <li>Dedicated project manager for each job, for better co-ordination of trades</li>
        <li>High-quality jobs</li>
        <li>Robust processes to ensure your project is well managed</li>
        <li>On time and on budget</li>
        <li>Responsive and timely communication</li>
        <li>Fair and competitive pricing</li>
        <li>Northcoat and Harlow accredited with volume discount, which means savings for our clients</li>
      </ul>
    </div>

    <div class="page-number page-number--right">7</div>
  </section>
</div>

<div class="spread spread--safety">
  <section class="page">
    <h1 class="page-heading" style="left:52px; top:48px;">
      <span class="accent">Safety &amp;</span><span class="base">Quality Assurance</span>
    </h1>
    <div class="dotted-rule" style="left:120px; top:97px; width:130px;"></div>
    <div class="dotted-stem" style="left:120px; top:97px; height:50px;"></div>
    <div class="block" style="left:132px; top:104px; width:340px;">
      <p>The safety of our workers and others is at the core of everything we do.</p>
      <p>We have compliant Workplace Health and Safety policies and procedures (including site inductions) in place and these are implemented at all times on every site.</p>
      <p><span class="em-brand">Brightwell Works</span> is committed to pursuing and achieving the best work safety practice.</p>
      <p>Safety is embedded in our daily practice. To ensure that we maintain our safety culture, we consult with employees regularly to see what's working and what isn't, and review our systems so we're improving every day.</p>
      <p style="font-weight:600;">Our primary goals are:</p>
      <ul class="bullets" style="margin-top:0;">
        <li>Elimination or mitigation of any risks and hazards in the workplace</li>
        <li>Provision of sufficient resources to relevant workplace safety regulations</li>
      </ul>
      <p style="font-weight:600; margin-top:10px;">Compliance Certificate –<br>Ausmark Trade Registry<br>Certificate Number 40517</p>
    </div>
    <div class="photo-rect" role="img" aria-label="Orange hard hat with ear defenders, safety glasses and work gloves" style="left:300px; top:270px; width:240px; height:170px; border-radius:50% 50% 30% 30%; background:radial-gradient(ellipse at 45% 40%, #ff8a2a, #e0561a 55%, rgba(255,255,255,0) 72%);"></div>
    <div class="page-number page-number--left">8</div>
  </section>

  <section class="page page--plain">
    <div class="brand" style="top:20px;">
      <div class="brand-name">Brightwell Works</div>
      <div class="brand-tag">strata painting &amp; remedial repair</div>
    </div>
    <div class="photo-rect" role="img" aria-label="Modern white two-storey house lit at dusk with large glass windows" style="left:0; top:58px; width:560px; height:180px; background:linear-gradient(170deg, #7b8fb3 0%, #c9bcc7 40%, #e9d7cf 60%, #9aa1b6 100%);"></div>

    <h2 class="page-heading" style="left:70px; top:256px;">
      <span class="accent">Environment</span>
    </h2>
    <div class="dotted-rule" style="left:112px; top:280px; width:150px;"></div>
    <div class="dotted-stem" style="left:112px; top:280px; height:40px;"></div>
    <div class="block" style="left:124px; top:286px; width:380px;">
      <p>At <span class="em-brand">Brightwell Works</span>, we acknowledge the importance of operating in a sustainable responsible manner.</p>
      <p>We take all reasonable care to minimise any harm to the environment, and review our systems regularly.</p>
      <p>This starts with the basics, like care of the property or site on which we're working. We extend this to care of the surroundings, chemicals management and safe disposal, and strict compliance with relevant legislation and regulations.</p>
      <p>All <span class="em-brand">Brightwell Works</span> staff/trades personnel exercise due diligence, are educated in environmental awareness and follow our environmental guidelines that include:</p>
      <ul class="bullets" style="margin-top:0;">
        <li>Site environmental plan</li>
        <li>Environmental action plan</li>
        <li>Environmental impact and safeguards statements</li>
      </ul>
      <p>Should an event occur that will harm, or has the potential to harm, the environment, <span class="em-brand">Brightwell Works</span> undertakes to notify the relevant authorities.</p>
    </div>
    <div class="page-number page-number--right">9</div>
  </section>
</div>

</body>
</html>
```